International E-Shop Needs a Web Design

I need a web design for a new e-shop based in UK, called Vornu. This will be an international collective buying website. I would like to see designs that use the colors orange and green (similar to logo colors). However, any other ideas and your vision are also welcome. The brand image is associated with words fun, social, cool and simple. The final design should look very modern and unique. Please also take into consideration user experience.

I have attached logo design. Please ignore the black background, it would be better if you extract only the name Vornu on the logo design. I have also attached one example of website design which I like (especially it's modern style, plumvexa.com) and two screenshots showing icons that visualize each category (which I want to appear in my main menu bar).

*UPDATE: There is something wrong with the system and I can't upload other 3 files (web design example and 2 examples of icons). If you could give me your e-mail, then I could send all these files to you. Anyway, what I think is a modern design can be viewed on plumvexa.com

If you have any further questions, do not hesitate to ask. Thank you in advance and I look forward to your outstanding designs!

Target Market(s)

My target customers are people both male and female in the age group of 18-45 years old, who are shopping online and are present on social media.

Industry/Entity Type

Shop

Requirements
Must have
• - "What is Vornu?" Button
- Log In / Register Buttons
- Currency Sliding Menu
- Shopping Cart
- "How to Buy?" and "How to Sell?" Buttons
- Follow us on Tralmonde, Quenzip, Brasko+
- Like Button with a number of people who like this.
- Check-In Button
- RSS Feed
- Main Menu with categories and buttons, such as Home, Electronics, Entertainment & Leisure, Fashion, Health & Beauty, Home & Garden, Jewellery & Watches, Sports & Outdoors. I would like to see also small pictures (icons) that would symbolize each category.
- Search Bar
- Carousel Slideshow with 5 different slides. The first slide on carousel slideshow should be welcoming! Something like: "Welcome to Vornu! Why to shop at Vornu?" - This slide should be designed in a similar way as the website.
- Four Main Categories: Latest Bargains, Your Recently Viewed Bargains, Ending Soon Bargains, Popular Bargains
- Under Each Category should be at least 3 products
- Users will be allowed to upload their own pictures, which means that picture quality and design will be different. Some kind of frames around pictures or something else (under one style) to make pictures look similar would be very helpful.
- Each Product should show the following information: Main Photo, Name, Description (Short), Total Discount (for example 35%), Current Discount (for example 5%), Starting Price, Current Price, Time Left on Bargain: 7:1:45:30
- The final design should be delivered in Photoshop format file (PSD file).
Should not have
• The choice of colors shouldn't be aggressive. Instead it should be calm and gentle. So that the user would feel himself comfortable while browsing the website.

```html
<!DOCTYPE html>
<html lang="en">
<head>
<meta charset="utf-8">
<title>Vornu — Collective Buying</title>
<link rel="stylesheet" href="https://fonts.googleapis.com/css2?family=Ubuntu:wght@400;500;700&family=Open+Sans:wght@400;600;700&display=swap">
<style>
:root{
  --orange:#f26a21;
  --orange-light:#f8912f;
  --orange-dark:#e85512;
  --amber:#f7a21b;
  --green:#7cc242;
  --green-dark:#5fa82c;
  --ink:#2b2b2b;
  --muted:#555;
  --line:#dcdcdc;
  --frame:#e4e4e4;
  --white:#fff;
}
*{box-sizing:border-box;margin:0;padding:0}
html,body{width:1200px;height:2419px;overflow:hidden;background:var(--white)}
body{position:relative;font-family:"Open Sans",Arial,sans-serif;color:var(--ink)}
.abs{position:absolute}
.top-strip{left:0;top:0;width:1200px;height:8px;background:var(--orange)}
.brand{left:24px;top:40px;font:700 56px/1 "Ubuntu",sans-serif;color:var(--orange);letter-spacing:-1px}
.checkin{left:382px;top:19px;width:131px;height:29px;border-radius:15px;background:var(--green);color:#fff;font:500 16px/29px "Ubuntu",sans-serif;display:flex;align-items:center;justify-content:center;gap:8px}
.search{left:382px;top:58px;width:410px;height:40px;border:1px solid var(--line);border-radius:4px;background:#fafafa;display:flex;align-items:center;font-size:14px;color:#666}
.search .all{flex:1;padding-left:16px;font-style:italic}
.search .cats{width:120px;border-left:1px solid var(--line);height:100%;display:flex;align-items:center;gap:8px;padding-left:10px;font-style:italic;color:#888}
.search .go{width:46px;height:46px;border-radius:50%;background:var(--green);margin-right:-4px;display:flex;align-items:center;justify-content:center}
.account-bar{left:826px;top:11px;width:350px;height:78px;border:1px solid var(--line);display:flex;background:#fff}
.account-bar>div{flex:1;border-right:1px solid var(--line);display:flex;flex-direction:column;align-items:center;justify-content:center;gap:6px;font-size:13px;text-align:center}
.account-bar>div:last-child{border-right:0}
.welcome{color:var(--green-dark);line-height:1.45}
.welcome .logout{color:var(--orange)}
.currency{left:845px;top:102px;width:313px;height:32px;border:1px solid var(--line);border-radius:3px;display:flex;align-items:center;gap:10px;padding-left:30px;font-size:14px}
.currency .flag{width:18px;height:12px;background:linear-gradient(#b22234 0 50%,#e8e8f0 50%);border-left:8px solid #3c3b6e}
.currency small{color:#999;font-size:11px}
.currency .caret{margin-left:auto;margin-right:16px}
.main-nav{left:13px;top:148px;width:1170px;height:105px;display:flex;background:linear-gradient(var(--orange-light),var(--orange-dark));border-radius:4px 4px 0 0}
.main-nav a{flex:1;color:#fff;text-decoration:none;font:400 18px "Ubuntu",sans-serif;display:flex;flex-direction:column;align-items:center;justify-content:center;gap:10px;border-right:1px solid rgba(255,255,255,.35)}
.main-nav a:last-child{border-right:0}
.main-nav a.current{background:rgba(0,0,0,.12)}
.hero{left:13px;top:253px;width:1170px;height:363px;border-left:1px solid var(--line);border-right:1px solid var(--line)}
.hero h1{position:absolute;left:32px;top:40px;font:500 26px "Ubuntu",sans-serif}
.hero p{position:absolute;left:42px;width:470px;font-size:13.5px;line-height:1.55;color:var(--muted)}
.hero .what{position:absolute;left:42px;top:244px;width:205px;height:47px;border-radius:8px;background:linear-gradient(#8ccf50,var(--green-dark));color:#fff;font:400 22px/47px "Ubuntu",sans-serif;display:flex;justify-content:center;align-items:center;gap:14px}
.hero .dots{position:absolute;left:44px;top:316px;display:flex;gap:5px}
.hero .dots i{width:12px;height:12px;border:2px solid var(--green)}
.hero .dots i.on{background:var(--green)}
.hero .devices{position:absolute;left:552px;top:37px;width:584px;height:278px;border-radius:10px;background:linear-gradient(135deg,#1c1c1c,#3d5a80 55%,#c9ccd2)}
.content{left:13px;top:616px;width:1170px;height:1678px;border:1px solid var(--line)}
.sidebar-rule{left:863px;top:616px;width:1px;height:1678px;background:var(--line)}
.section{position:absolute;left:32px;width:813px}
.section h2{font:400 22px "Ubuntu",sans-serif;margin-bottom:26px}
.deals{display:flex;gap:18px}
.deal{width:190px}
.deal-photo{position:relative;width:190px;height:162px;border:4px solid var(--frame);background:#fff;padding:6px}
.deal-photo .shot{width:100%;height:100%;background:var(--tone)}
.deal-photo .badge{position:absolute;left:6px;right:6px;bottom:6px;height:42px;background:rgba(30,30,30,.85);color:#fff;font-size:12.5px;text-align:center;line-height:20px;padding-top:1px}
.deal h3{margin-top:12px;font:700 14.5px "Open Sans",sans-serif;color:var(--orange)}
.deal .blurb{font-size:13px;line-height:1.4;color:var(--ink);margin-top:2px}
.deal .meta{font-size:13px;line-height:1.55}
.deal .meta b{color:var(--orange);font-size:19px;font-weight:600}
.rule{position:absolute;left:32px;width:813px;height:1px;background:var(--line)}
.side-btn{left:866px;width:316px;height:53px;border-radius:4px;color:#fff;font:500 20px/53px "Ubuntu",sans-serif;display:flex;align-items:center;gap:22px;padding-left:14px}
.side-btn.buy{top:637px;background:linear-gradient(#fbb03b,var(--amber))}
.side-btn.sell{top:698px;background:linear-gradient(#8ccf50,var(--green-dark))}
.my-account{left:866px;top:765px;width:316px;height:44px;background:var(--orange);color:#fff;font:400 20px/44px "Ubuntu",sans-serif;padding-left:20px}
.cart-box{left:875px;top:820px;width:300px;height:140px;font-size:14px}
.cart-box .wish{position:absolute;left:104px;top:6px;color:var(--muted)}
.cart-box .mycart{position:absolute;left:104px;top:40px;font-weight:700}
.cart-box .total{position:absolute;left:104px;top:70px;color:var(--orange);font-size:21px}
.cart-box .checkout{position:absolute;left:104px;top:106px;width:142px;height:26px;border-radius:13px;background:linear-gradient(#fbb03b,#f38f14);border:1px solid #d97a0a;font-size:13px;display:flex;align-items:center;justify-content:center;gap:6px}
.panel{left:873px;width:304px;border:1px solid var(--line);background:#fff}
.like-panel{top:977px;height:107px;display:flex;align-items:center;padding-left:22px;gap:20px}
.like-panel .mini-brand{font:700 28px "Ubuntu",sans-serif;color:var(--orange)}
.like-panel .count{font-size:13px}
.like-panel .like{display:inline-block;margin-top:10px;background:var(--amber);color:#fff;padding:2px 16px;font-size:14px;border-radius:2px}
.follow-panel{top:1097px;height:105px;padding:10px 20px}
.follow-panel h4{font:400 16px "Open Sans",sans-serif;margin-bottom:10px}
.socials{display:flex;gap:13px}
.socials span{width:42px;height:42px;border-radius:50%;border:1px solid #ccc;background:linear-gradient(#fff,#eee);font:700 15px/40px "Open Sans",sans-serif;text-align:center;color:var(--muted)}
.rss-head{top:1221px;height:42px;font:400 22px/40px "Ubuntu",sans-serif;padding-left:14px}
.rss{left:883px;top:1273px;width:300px}
.rss h5{font:600 15px "Open Sans",sans-serif;margin-top:12px}
.rss p{font-size:13px;line-height:1.55;margin-top:4px}
.footer{left:13px;top:2310px;width:1170px;height:109px;background:linear-gradient(var(--orange-light),var(--orange-dark));color:#fff;padding:14px 25px;font-size:15px;border-radius:4px 4px 0 0}
.footer nav{display:flex;gap:8px}
.footer .copy{margin-top:16px}
.footer .fsocial{position:absolute;right:30px;top:14px;display:flex;gap:6px}
.footer .fsocial span{width:28px;height:28px;border-radius:50%;background:#fff;color:var(--orange);font:700 13px/28px "Open Sans",sans-serif;text-align:center}
</style>
</head>
<body>
<div class="abs top-strip"></div>
<div class="abs brand">Vornu</div>

<div class="abs checkin">
  <svg width="18" height="16" viewBox="0 0 18 16"><path d="M2 8l5 5L16 3" stroke="#fff" stroke-width="3" fill="none"/></svg>Check-In
</div>
<div class="abs search">
  <span class="all">All</span>
  <span class="cats"><svg width="10" height="8"><path d="M0 0h10L5 7z" fill="#999"/></svg>Categories</span>
  <span class="go"><svg width="20" height="20" viewBox="0 0 20 20"><circle cx="8" cy="8" r="5.5" stroke="#fff" stroke-width="2.5" fill="none"/><path d="M12 12l5 5" stroke="#fff" stroke-width="3"/></svg></span>
</div>

<div class="abs account-bar">
  <div>
    <svg width="36" height="30" viewBox="0 0 36 30"><path d="M2 3h6l4 17h18l4-12H10" stroke="#5fa82c" stroke-width="3" fill="none"/><circle cx="14" cy="26" r="3" fill="#5fa82c"/><circle cx="27" cy="26" r="3" fill="#5fa82c"/></svg>
    Shopping Cart
  </div>
  <div class="welcome">Welcome ,<br>Marel!<br><span class="logout">Not You? / Log Out</span></div>
  <div>
    <svg width="32" height="32" viewBox="0 0 32 32"><circle cx="14" cy="10" r="7" fill="#bbb"/><path d="M2 30c0-8 6-12 12-12s12 4 12 12z" fill="#ccc"/><path d="M26 18v10M21 23h10" stroke="#5fa82c" stroke-width="3"/></svg>
    Register User
  </div>
</div>
<div class="abs currency"><span class="flag"></span>$ 00.00 &nbsp;USD <small>US dollar</small><svg class="caret" width="14" height="9"><path d="M0 0h14L7 8z" fill="#7cc242"/></svg></div>

<nav class="abs main-nav">
  <a class="current" href="#"><svg width="38" height="34" viewBox="0 0 38 34"><path d="M19 2L2 17h5v15h9v-9h6v9h9V17h5z" fill="#fff"/></svg>Home</a>
  <a href="#"><svg width="44" height="34" viewBox="0 0 44 34"><rect x="7" y="3" width="30" height="21" rx="2" stroke="#fff" stroke-width="3" fill="none"/><path d="M1 28h42l-3 4H4z" fill="#fff"/></svg>Electronics</a>
  <a href="#"><svg width="38" height="34" viewBox="0 0 38 34"><rect x="3" y="3" width="32" height="28" stroke="#fff" stroke-width="3" fill="none"/><path d="M8 26l8-10 6 6 4-4 6 8z" fill="#fff"/><circle cx="27" cy="11" r="3" fill="#fff"/></svg>Entertainment</a>
  <a href="#"><svg width="30" height="36" viewBox="0 0 30 36"><path d="M15 2c2 8 12 12 12 22a12 12 0 01-24 0C3 16 10 14 15 2z" fill="#fff"/><path d="M15 18c1 5 6 6 6 11a6 6 0 01-12 0c0-4 4-6 6-11z" fill="#f26a21"/></svg>Fashion</a>
  <a href="#"><svg width="36" height="36" viewBox="0 0 36 36"><circle cx="18" cy="18" r="15" stroke="#fff" stroke-width="3" fill="none"/><path d="M18 9v18M9 18h18" stroke="#fff" stroke-width="5"/></svg>Health &amp; Beauty</a>
  <a href="#"><svg width="36" height="36" viewBox="0 0 36 36"><circle cx="18" cy="18" r="15" stroke="#fff" stroke-width="3" fill="none"/><path d="M18 8v10h8" stroke="#fff" stroke-width="3" fill="none"/></svg>Jewellery &amp; Watches</a>
  <a href="#"><svg width="52" height="36" viewBox="0 0 52 36"><circle cx="11" cy="25" r="9" stroke="#fff" stroke-width="3" fill="none"/><circle cx="41" cy="25" r="9" stroke="#fff" stroke-width="3" fill="none"/><path d="M11 25l9-13h15l6 13M20 12l7 13h-16M33 5h4v7" stroke="#fff" stroke-width="3" fill="none"/><circle cx="33" cy="4" r="3" fill="#fff"/></svg>Sports &amp; Outdoor</a>
</nav>

<section class="abs hero">
  <h1>"Welcome to Vornu! Why to shop at Vornu?"</h1>
  <p style="top:88px">Lorem ipsum dolor sit amet, consectetuer adipiscing elit. Nam cursus. Morbi ut mi. Nullam enim leo, egestas id, condimentum at, laoreet matti.s, massa.</p>
  <p style="top:143px">Sed eleifend nonummy diam. Praesent mauris ante, elementum et, bibendum at, posuere sit amet, nibh. Duis tincidunt lectus quis dui viverra vestibulum. Suspendisse vulputate aliquam dui. Nulla elementum dui ut augue. Aliquam vehicula mi at mauris.</p>
  <div class="what">What is Vornu? <svg width="8" height="10"><path d="M0 0l8 5-8 5z" fill="#fff"/></svg></div>
  <div class="dots"><i class="on"></i><i></i><i></i><i></i><i></i></div>
  <div class="devices" role="img" aria-label="Tablet, laptop and phone showing the Vornu site"></div>
</section>

<div class="abs content"></div>
<div class="abs sidebar-rule"></div>

<section class="section" style="top:645px">
  <h2>Latest Bargains</h2>
  <div class="deals">
    <article class="deal"><div class="deal-photo"><div class="shot" role="img" aria-label="Netbook computer" style="--tone:linear-gradient(#1a8fb8,#222)"></div><div class="badge">Current Discount 18%<br>Current Price $250</div></div><h3>Name of Products</h3><p class="blurb">Lorem ipsum dolor sit amet, consectetuer adipiscing elit.</p><p class="meta">Discount <b>55%</b></p><p class="meta">Price range &nbsp;$85 to &nbsp;$150</p><p class="meta">Time left &nbsp;&nbsp;3:1:45:30</p></article>
    <article class="deal"><div class="deal-photo"><div class="shot" role="img" aria-label="Compact speaker system" style="--tone:linear-gradient(#f4f4f4,#cfcfcf)"></div></div><h3>Name of Products</h3><p class="blurb">Lorem ipsum dolor sit amet, consectetuer adipiscing elit.</p><p class="meta">Discount <b>55%</b></p><p class="meta">Price range &nbsp;$85 to &nbsp;$150</p><p class="meta">Time left &nbsp;&nbsp;7:1:45:30</p></article>
    <article class="deal"><div class="deal-photo"><div class="shot" role="img" aria-label="Stack of towels" style="--tone:linear-gradient(#e05a9a,#555)"></div></div><h3>Name of Products</h3><p class="blurb">Lorem ipsum dolor sit amet, consectetuer adipiscing elit.</p><p class="meta">Discount <b>55%</b></p><p class="meta">Price range &nbsp;$85 to &nbsp;$150</p><p class="meta">Time left &nbsp;&nbsp;7:5:45:30</p></article>
    <article class="deal"><div class="deal-photo"><div class="shot" role="img" aria-label="Kitchen blender set" style="--tone:linear-gradient(#eef2f6,#c4ccd6)"></div></div><h3>Name of Products</h3><p class="blurb">Lorem ipsum dolor sit amet, consectetuer adipiscing elit.</p><p class="meta">Discount <b>55%</b></p><p class="meta">Price range &nbsp;$85 to &nbsp;$150</p><p class="meta">Time left &nbsp;&nbsp;5:1:45:30</p></article>
  </div>
</section>
<div class="rule" style="top:1032px"></div>

<section class="section" style="top:1063px">
  <h2>Your Recently Viewed Bargains</h2>
  <div class="deals">
    <article class="deal"><div class="deal-photo"><div class="shot" role="img" aria-label="Wireless headphones" style="--tone:linear-gradient(#555,#111)"></div></div><h3>Name of Products</h3><p class="blurb">Lorem ipsum dolor sit amet, consectetuer adipiscing elit.</p><p class="meta">Maximum Discount <b>55%</b></p><p class="meta">Price range &nbsp;$85 to &nbsp;$150</p><p class="meta">Time left &nbsp;&nbsp;1:1:45:30</p></article>
    <article class="deal"><div class="deal-photo"><div class="shot" role="img" aria-label="USB flash drive" style="--tone:linear-gradient(135deg,#ddd,#7d7d7d)"></div></div><h3>Name of Products</h3><p class="blurb">Lorem ipsum dolor sit amet, consectetuer adipiscing elit.</p><p class="meta">Maximum Discount <b>55%</b></p><p class="meta">Price range &nbsp;$85 to &nbsp;$150</p><p class="meta">Time left &nbsp;&nbsp;7:1:45:30</p></article>
    <article class="deal"><div class="deal-photo"><div class="shot" role="img" aria-label="Gas stove" style="--tone:linear-gradient(#bbb,#2a2a2a)"></div></div><h3>Name of Products</h3><p class="blurb">Lorem ipsum dolor sit amet, consectetuer adipiscing elit.</p><p class="meta">Maximum Discount <b>55%</b></p><p class="meta">Price range &nbsp;$85 to &nbsp;$150</p><p class="meta">Time left &nbsp;&nbsp;2:1:45:30</p></article>
    <article class="deal"><div class="deal-photo"><div class="shot" role="img" aria-label="Power drill" style="--tone:linear-gradient(#f2f2f2,#2d3f7a)"></div></div><h3>Name of Products</h3><p class="blurb">Lorem ipsum dolor sit amet, consectetuer adipiscing elit.</p><p class="meta">Maximum Discount <b>55%</b></p><p class="meta">Price range &nbsp;$85 to &nbsp;$150</p><p class="meta">Time left &nbsp;&nbsp;7:1:45:30</p></article>
  </div>
</section>
<div class="rule" style="top:1458px"></div>

<section class="section" style="top:1487px">
  <h2>Closing Soon Bargains</h2>
  <div class="deals">
    <article class="deal"><div class="deal-photo"><div class="shot" role="img" aria-label="Beaded necklace with pendant" style="--tone:linear-gradient(#f5f5f5,#3a9aa6)"></div></div><h3>Name of Products</h3><p class="blurb">Lorem ipsum dolor sit amet, consectetuer adipiscing elit.</p><p class="meta">Maximum Discount <b>55%</b></p><p class="meta">Price range &nbsp;$85 to &nbsp;$150</p><p class="meta">Time left &nbsp;&nbsp;1:1:45:30</p></article>
    <article class="deal"><div class="deal-photo"><div class="shot" role="img" aria-label="Toy race track" style="--tone:linear-gradient(#f7e04a,#8a54b6)"></div></div><h3>Name of Products</h3><p class="blurb">Lorem ipsum dolor sit amet, consectetuer adipiscing elit.</p><p class="meta">Maximum Discount <b>55%</b></p><p class="meta">Price range &nbsp;$85 to &nbsp;$150</p><p class="meta">Time left &nbsp;&nbsp;7:1:45:30</p></article>
    <article class="deal"><div class="deal-photo"><div class="shot" role="img" aria-label="Compact digital camera" style="--tone:linear-gradient(#666,#111)"></div></div><h3>Name of Products</h3><p class="blurb">Lorem ipsum dolor sit amet, consectetuer adipiscing elit.</p><p class="meta">Maximum Discount <b>55%</b></p><p class="meta">Price range &nbsp;$85 to &nbsp;$150</p><p class="meta">Time left &nbsp;&nbsp;2:1:45:30</p></article>
    <article class="deal"><div class="deal-photo"><div class="shot" role="img" aria-label="Running shoes" style="--tone:linear-gradient(#eef0f6,#2b3163)"></div></div><h3>Name of Products</h3><p class="blurb">Lorem ipsum dolor sit amet, consectetuer adipiscing elit.</p><p class="meta">Maximum Discount <b>55%</b></p><p class="meta">Price range &nbsp;$85 to &nbsp;$150</p><p class="meta">Time left &nbsp;&nbsp;7:1:45:30</p></article>
  </div>
</section>
<div class="rule" style="top:1885px;left:13px;width:850px"></div>

<section class="section" style="top:1911px">
  <h2>Closing Soon Bargains</h2>
  <div class="deals">
    <article class="deal"><div class="deal-photo"><div class="shot" role="img" aria-label="Beaded necklace with pendant" style="--tone:linear-gradient(#f5f5f5,#3a9aa6)"></div></div><h3>Name of Products</h3><p class="blurb">Lorem ipsum dolor sit amet, consectetuer adipiscing elit.</p><p class="meta">Maximum Discount <b>55%</b></p><p class="meta">Price range &nbsp;$85 to &nbsp;$150</p><p class="meta">Time left &nbsp;&nbsp;1:1:45:30</p></article>
    <article class="deal"><div class="deal-photo"><div class="shot" role="img" aria-label="Toy race track" style="--tone:linear-gradient(#f7e04a,#8a54b6)"></div></div><h3>Name of Products</h3><p class="blurb">Lorem ipsum dolor sit amet, consectetuer adipiscing elit.</p><p class="meta">Maximum Discount <b>55%</b></p><p class="meta">Price range &nbsp;$85 to &nbsp;$150</p><p class="meta">Time left &nbsp;&nbsp;7:1:45:30</p></article>
    <article class="deal"><div class="deal-photo"><div class="shot" role="img" aria-label="Compact digital camera" style="--tone:linear-gradient(#666,#111)"></div></div><h3>Name of Products</h3><p class="blurb">Lorem ipsum dolor sit amet, consectetuer adipiscing elit.</p><p class="meta">Maximum Discount <b>55%</b></p><p class="meta">Price range &nbsp;$85 to &nbsp;$150</p><p class="meta">Time left &nbsp;&nbsp;2:1:45:30</p></article>
    <article class="deal"><div class="deal-photo"><div class="shot" role="img" aria-label="Running shoes" style="--tone:linear-gradient(#eef0f6,#2b3163)"></div></div><h3>Name of Products</h3><p class="blurb">Lorem ipsum dolor sit amet, consectetuer adipiscing elit.</p><p class="meta">Maximum Discount <b>55%</b></p><p class="meta">Price range &nbsp;$85 to &nbsp;$150</p><p class="meta">Time left &nbsp;&nbsp;7:1:45:30</p></article>
  </div>
</section>

<div class="abs side-btn buy"><svg width="34" height="28" viewBox="0 0 34 28"><path d="M2 10h30l-4 16H6z" fill="#fff"/><path d="M9 10l6-8M25 10l-6-8" stroke="#fff" stroke-width="3"/></svg>HOW TO BUY ?</div>
<div class="abs side-btn sell"><svg width="32" height="32" viewBox="0 0 32 32"><circle cx="16" cy="16" r="13" stroke="#fff" stroke-width="3" fill="none"/><text x="16" y="22" text-anchor="middle" font-family="Open Sans" font-weight="700" font-size="17" fill="#fff">$</text></svg>HOW TO SELL?</div>
<div class="abs my-account">My Account</div>
<div class="abs cart-box">
  <svg class="abs" style="left:12px;top:28px" width="56" height="50" viewBox="0 0 56 50"><path d="M2 4h9l6 28h30l6-20H14" stroke="#aaa" stroke-width="3" fill="none" stroke-dasharray="4 2"/><circle cx="21" cy="42" r="4" fill="#aaa"/><circle cx="43" cy="42" r="4" fill="#aaa"/></svg>
  <span class="wish">My Wish List</span>
  <span class="mycart">My Cart - ( 0 ) Items</span>
  <span class="total">Total - $ 00.00</span>
  <span class="checkout"><svg width="14" height="12"><rect x="1" y="1" width="11" height="10" stroke="#333" fill="none"/><path d="M3 6l3 3 7-8" stroke="#333" stroke-width="1.6" fill="none"/></svg>Check out</span>
</div>
<div class="abs panel like-panel">
  <span class="mini-brand">Vornu</span>
  <div><div class="count">2188 people like this</div><span class="like">Like</span></div>
</div>
<div class="abs panel follow-panel">
  <h4>Follow Us On</h4>
  <div class="socials"><span title="Tralmonde">T</span><span title="Quenzip">Q</span><span title="Brasko+">B+</span><span title="Linqra">L</span><span title="RSS"><svg width="18" height="18" viewBox="0 0 18 18" style="margin-top:11px"><circle cx="3" cy="15" r="2.5" fill="#f26a21"/><path d="M1 8a9 9 0 019 9M1 2a15 15 0 0115 15" stroke="#f26a21" stroke-width="2.5" fill="none"/></svg></span></div>
</div>
<div class="abs panel rss-head">Rss Feed</div>
<div class="abs rss">
  <h5>Tittle line goes here</h5>
  <p>Lorem ipsum dolor sit amet, consectetuer adipiscing elit. Nam cursus. Morbi ut mi. Nullam enim leo, egestas id, condimentum at</p>
  <h5 style="margin-top:26px">Tittle line goes here</h5>
  <p>auris vel lacus vitae felis vestibulum volutpat. Etiam est nunc, venenatis in, tristique eu, imperdiet ac, nisl. Cum sociis natoque penatibus et magnis dis parturient montes, nascetur ridiculus mus. In iaculis facilisis massa. Etiam eu urna. Sed porta. Suspendisse quam leo, molestie sed, luctus quis, feugiat in, pede.</p>
  <h5 style="margin-top:26px">Tittle line goes here</h5>
  <p>Aliquam vehicula mi at mauris. Maecenas placerat, nisl at consequat rhoncus, sem nunc gravida justo, quis eleifend arcu velit quis lacus</p>
  <h5 style="margin-top:26px">Tittle line goes here</h5>
  <p>Praesent vitae lacus. Ut velit enim, vestibulum non, fermentum nec, hendrerit quis, leo. Pellentesque rutrum malesuada neque.<br>Nunc tempus felis vitae urna. Vivamus porttitor, neque at volutpat rutrum, purus nisi eleifend libero, a tempus libero lectus feugiat felis.</p>
</div>

<footer class="abs footer">
  <nav><span>Home</span>|<span>Products</span>|<span>What We Are</span>|<span>Rss Feed</span>|<span>Special</span>|<span>Sitemap</span>|<span>Contact</span></nav>
  <div class="copy">© 2012 Company Name &nbsp;| &nbsp;All right resreved</div>
  <div class="fsocial"><span>R</span><span>T</span><span>Q</span><span>L</span></div>
</footer>
</body>
</html>
```